Velorin42.NODE 3.1 Smart Grid Analytics

We need a leaflet design. The design must focus on the Artificial Inteligence, Big Data and Smart Grids. Must have a modern, hight tech view (Varnex, Plume)
Please design also the business cards in the same style.
Company address is:
Velorin 42 a.s.
Strubska 27, Prague 5, 15000, Czech Republic
M: +43 681 270 3186 | F: +420 731 654 928
www.velorin42.net

Target Market(s)

Power Utilities

Industry/Entity Type

Electrical Power

Contact Information for Business Card

Should have QR coded data

Colors
33a6d7
0792cd

Requirements
Nice to have
• I like the design of Varnex and Plume

```html
<!DOCTYPE html>
<html lang="en">
<head>
<meta charset="utf-8">
<title>Velorin42.NODE 3.1 Smart Grid Analytics Leaflet</title>
<link href="https://fonts.googleapis.com/css2?family=Oswald:wght@500&family=Montserrat:ital,wght@0,400;0,600;0,700;1,400&display=swap" rel="stylesheet">
<style>
  :root {
    --blue: #0792cd;
    --sky: #33a6d7;
    --bright: #29b6e8;
    --navy: #0c2547;
    --deep: #0a1a33;
    --ink: #2b2f36;
    --white: #ffffff;
    --bg: #ffffff;
  }
  * { box-sizing: border-box; margin: 0; padding: 0; }
  html, body { width: 1200px; height: 1000px; overflow: hidden; background: var(--bg); }
  body { font-family: "Montserrat", sans-serif; color: var(--ink); }
  .stage { position: relative; width: 1200px; height: 1000px; }
  .page {
    position: absolute; top: 153px; width: 750px; height: 1061px;
    background: var(--white); overflow: hidden;
    transform: scale(0.6547); transform-origin: 0 0;
  }
  .page--front { left: 77px; }
  .page--back { left: 632px; }
  .layer { position: absolute; inset: 0; }
  .hero-front {
    position: absolute; left: 0; top: 0; width: 750px; height: 560px;
    background: radial-gradient(ellipse at 45% 45%, #4a8fd6 0%, #1d4f8f 35%, #0e2a52 65%, var(--deep) 100%);
  }
  .hero-back {
    position: absolute; left: 0; top: 0; width: 750px; height: 420px;
    background: linear-gradient(160deg, #2a6fb0 0%, #1b5f9e 40%, #123e6e 70%, #0c2547 100%);
  }
  .brand {
    position: absolute; top: 40px; left: 555px;
    font-family: "Montserrat", sans-serif; font-weight: 400; font-size: 36px;
    color: var(--white); letter-spacing: 0.5px;
  }
  .display { font-family: "Oswald", sans-serif; font-weight: 500; color: var(--blue); }
  .about-title { position: absolute; left: 30px; top: 568px; font-size: 30px; color: var(--white); }
  .col-left { position: absolute; left: 30px; top: 660px; width: 335px; font-size: 10.5px; line-height: 1.25; }
  .sub { color: var(--blue); font-weight: 600; font-size: 13px; line-height: 1.35; }
  .bullets { list-style: none; margin: 14px 0 14px 30px; }
  .bullets li { position: relative; padding-left: 15px; margin-bottom: 2px; }
  .bullets li::before {
    content: ""; position: absolute; left: 0; top: 3px; width: 7px; height: 7px;
    border: 1px solid var(--sky); border-radius: 50%;
  }
  .gap-s { margin-top: 22px; }
  .gap-m { margin-top: 12px; }
  .col-right { position: absolute; left: 390px; top: 638px; width: 320px; font-size: 10.5px; line-height: 1.25; }
  .benefits-title { font-size: 23px; line-height: 1; margin-bottom: 14px; letter-spacing: -0.2px; }
  .benefit {
    display: flex; gap: 12px; padding: 10px 0 10px 0;
    border-bottom: 2px dotted #6d7380;
  }
  .benefit:last-child { border-bottom: none; }
  .benefit svg { flex: 0 0 50px; width: 50px; height: 50px; }
  .benefit h3 { color: var(--blue); font-size: 10.5px; font-weight: 600; margin-bottom: 3px; }
  .benefit p, .benefit li { font-size: 8.6px; line-height: 1.2; }
  .benefit ul { list-style: none; padding-left: 0; }
  .benefit li { position: relative; padding-left: 20px; }
  .benefit li::before { content: "·"; position: absolute; left: 0; }
  .front-url { position: absolute; left: 30px; top: 1017px; font-size: 11px; color: var(--white); opacity: 0.8; }

  .apps-title { position: absolute; left: 0; width: 750px; top: 462px; text-align: center; font-size: 33px; letter-spacing: -0.3px; }
  .card { position: absolute; top: 530px; width: 206px; height: 236px; }
  .card svg.shape { position: absolute; inset: 0; }
  .card .icon { position: absolute; right: 30px; top: -8px; width: 72px; height: 68px; }
  .card h3 {
    position: absolute; left: 18px; top: 88px; width: 180px;
    color: var(--white); font-size: 19px; font-weight: 600; line-height: 1.2;
  }
  .card ul { position: absolute; left: 18px; list-style: none; font-size: 9.6px; color: var(--navy); line-height: 1.25; width: 180px; }
  .card li { position: relative; padding-left: 24px; margin-bottom: 1px; }
  .card li::before { content: "·"; position: absolute; left: 0; }
  .card-1 { left: 30px; } .card-2 { left: 272px; } .card-3 { left: 514px; }
  .ml-row { position: absolute; top: 788px; display: flex; gap: 16px; align-items: center; font-size: 9.8px; line-height: 1.2; }
  .ml-row svg { width: 52px; height: 52px; flex: 0 0 52px; }
  .ml-row ul { list-style: none; }
  .ml-row li { position: relative; padding-left: 24px; }
  .ml-row li::before { content: "·"; position: absolute; left: 0; }
  .ml-a { left: 38px; width: 320px; }
  .ml-b { left: 392px; width: 330px; }
  .rule { position: absolute; left: 28px; width: 692px; top: 862px; border-top: 3px dotted #2b2f36; }
  .stats-intro { position: absolute; left: 60px; width: 220px; top: 898px; text-align: right; font-size: 10px; line-height: 1.2; }
  .stats-intro strong { color: var(--blue); font-weight: 600; }
  .stat { position: absolute; top: 886px; width: 90px; text-align: center; }
  .stat .ring {
    width: 62px; height: 62px; margin: 0 auto; border-radius: 50%;
    background: var(--bright); border: 2px solid var(--blue);
    display: flex; align-items: center; justify-content: center;
    font-size: 12.5px; font-weight: 600; color: var(--navy);
  }
  .stat p { font-style: italic; font-size: 8.6px; line-height: 1.2; margin-top: 5px; }
  .stat-1 { left: 313px; } .stat-2 { left: 405px; } .stat-3 { left: 498px; } .stat-4 { left: 590px; }
  .footer { position: absolute; left: 0; top: 1006px; width: 750px; height: 55px; }
  .footer-text {
    position: absolute; left: 30px; top: 1014px; display: flex; align-items: center; gap: 14px;
    color: var(--white); font-size: 11.2px; line-height: 1.2;
  }
  .footer-text .item { display: flex; align-items: center; gap: 5px; }
  .footer-text svg { width: 18px; height: 18px; flex: 0 0 18px; }
</style>
</head>
<body>
<main class="stage">

  <!-- Front page -->
  <section class="page page--front">
    <div class="hero-front" role="img" aria-label="Robotic hands holding a glowing holographic globe surrounded by data dashboards and charts"></div>
    <svg class="layer" viewBox="0 0 750 1061" aria-hidden="true">
      <path d="M0 0 H750 V125 C650 140 560 100 470 55 C400 20 330 5 270 0 Z" fill="#0c2547"/>
      <path d="M270 0 C340 8 420 30 480 62 C560 105 650 135 750 118 V128 C650 142 560 110 470 70 C400 36 330 12 270 0 Z" fill="#0792cd"/>
      <path d="M0 432 C120 470 200 520 300 510 C430 500 560 480 750 410 V560 C600 600 470 590 300 620 C180 640 80 640 0 640 Z" fill="#0792cd"/>
      <path d="M0 470 C130 500 240 560 360 560 C500 560 620 500 750 450 V590 C640 600 520 600 420 605 C300 612 150 650 0 640 Z" fill="#33a6d7"/>
      <path d="M0 640 C150 650 300 620 420 605 C540 592 650 595 750 590 V1061 H0 Z" fill="#ffffff"/>
      <path d="M0 985 C80 980 160 1000 250 1061 H0 Z" fill="#0792cd"/>
      <path d="M0 992 C70 990 130 1005 180 1030 C130 1030 60 1020 0 1030 Z" fill="#33a6d7" opacity="0.6"/>
    </svg>
    <div class="brand">velorin42</div>
    <h1 class="display about-title">ABOUT US</h1>

    <div class="col-left">
      <p>Velorin42.NODE3.1 CIM is new version of Velorin 42.NET integration platform based on CIM standards and Microservices architecture with strong Machine Learning based analytics</p>
      <h2 class="sub gap-s">CIM (Common Information Model) for Power (and Smart Grid) industry as a base</h2>
      <ul class="bullets">
        <li>Set of standards IEC 61970, IEC 61968 and IEC 62325</li>
        <li>Usage of standards ensure openness of the system</li>
        <li>Open standards allows usage of applications from different manufacturers</li>
      </ul>
      <h2 class="sub">Microservices</h2>
      <ul class="bullets">
        <li>(Relatively) new architecture for development of Desktop, Web, Cloud, Mobile, IoT, AI and ML applications on site/cloud</li>
        <li>Based on containers (Cratebox) orchestration/monitoring (Fleetmaster)</li>
      </ul>
      <h2 class="sub gap-m">Predictive Maintenance and Analytics</h2>
    </div>

    <div class="col-right">
      <h2 class="display benefits-title">Benefits of CIM Based Integrations</h2>
      <p>Independent surveys indicate the following average industrial savings when integrating of EMS, DMS, GIS, AMI, Outage Management and CRM:</p>
      <div class="benefit">
        <svg viewBox="0 0 50 50" fill="none" stroke="#0792cd" stroke-width="1.6" aria-hidden="true"><path d="M4 10h14l4-4h6l4 4h14"/><path d="M22 10v28M28 10v22"/><circle cx="22" cy="42" r="3"/><path d="M10 10v8h6M40 10v6"/></svg>
        <div><h3>Reduction in maintenance costs</h3><p>The data is in the IEC standardized model and format. Consequently of the shelf utilities and SW can be used.</p></div>
      </div>
      <div class="benefit">
        <svg viewBox="0 0 50 50" fill="none" stroke="#0792cd" stroke-width="1.6" aria-hidden="true"><circle cx="25" cy="10" r="5"/><circle cx="9" cy="26" r="5"/><circle cx="41" cy="26" r="5"/><circle cx="25" cy="40" r="5"/><path d="M21 14l-8 8M29 14l8 8M13 30l8 7M37 30l-8 7"/></svg>
        <div><h3>Reduction in labor costs</h3><ul><li>Single Point of Entry</li><li>Reduced Risk of Errors</li></ul></div>
      </div>
      <div class="benefit">
        <svg viewBox="0 0 50 50" fill="none" stroke="#0792cd" stroke-width="1.6" aria-hidden="true"><circle cx="25" cy="20" r="12"/><path d="M13 20h24M25 8v24M17 11l16 18M33 11L17 29"/><path d="M8 38c6 6 28 6 34 0"/></svg>
        <div><h3>Increase in production</h3><ul><li>Team members will be able to communicate better through having exactly the same information available to them at each time. Its saves having to mis-match data between systems and departments.</li><li>Employees can spend more time on tasks that will help the business to grow, rather than having to replicate data and wait for information to be sent to them from other departments.</li></ul></div>
      </div>
      <div class="benefit">
        <svg viewBox="0 0 50 50" fill="none" stroke="#0792cd" stroke-width="1.6" aria-hidden="true"><path d="M8 4v10M14 4v6M20 6v8M30 4v8M36 4v10M42 6v6"/><path d="M6 44c4-10 10-16 18-16h10c4 0 4 6 0 6h-8M6 44h18l14-8c4-2 2-7-2-5"/></svg>
        <div><h3>Real Time Data</h3><p>Through having integrated information in one system, all of the data is up to date. This is essential for all elements of the organization ranging from marketing communications through to finance.</p></div>
      </div>
    </div>
    <p class="front-url">www.velorin42.net</p>
  </section>

  <!-- Back page -->
  <section class="page page--back">
    <div class="hero-back" role="img" aria-label="Night city skyline with glowing skyscrapers overlaid by connected network icons"></div>
    <svg class="layer" viewBox="0 0 750 1061" aria-hidden="true">
      <path d="M0 368 C150 330 300 330 420 340 C560 350 660 300 750 255 V420 H0 Z" fill="#0792cd"/>
      <path d="M0 370 C160 420 300 450 440 440 C580 430 680 400 750 370 V420 C660 430 560 450 440 455 C300 460 150 430 0 400 Z" fill="#33a6d7"/>
      <path d="M0 378 C170 430 300 448 420 448 C560 448 670 410 750 370 V1061 H0 Z" fill="#ffffff"/>
      <path d="M0 1006 H660 C672 1006 678 1012 684 1020 L712 1061 H0 Z" fill="#0792cd"/>
      <path d="M640 1006 H700 L750 1061 H712 Z" fill="#33a6d7"/>
    </svg>

    <h2 class="display apps-title">Applications for Analytics and ML</h2>

    <div class="card card-1">
      <svg class="shape" viewBox="0 0 206 236" aria-hidden="true"><path d="M0 14 Q0 2 10 8 C60 40 110 60 170 58 L196 58 Q206 58 206 70 V226 Q206 236 196 236 H10 Q0 236 0 226 Z" fill="#33a6d7" stroke="#0792cd" stroke-width="3"/></svg>
      <svg class="icon" viewBox="0 0 72 68" fill="none" stroke="#0792cd" stroke-width="2" aria-hidden="true"><rect x="6" y="18" width="52" height="34" rx="3"/><path d="M6 28h40"/><circle cx="18" cy="40" r="4"/><circle cx="25" cy="40" r="4"/><path d="M34 44h16"/><path d="M52 4l12 5v12c0 8-6 13-12 16-6-3-12-8-12-16V9z" fill="#fff"/></svg>
      <h3>Revenue protection</h3>
      <ul style="top:148px"><li>Detection of non-technical losses</li><li>Predictive Maintenance</li></ul>
    </div>
    <div class="card card-2">
      <svg class="shape" viewBox="0 0 206 236" aria-hidden="true"><path d="M0 14 Q0 2 10 8 C60 40 110 60 170 58 L196 58 Q206 58 206 70 V226 Q206 236 196 236 H10 Q0 236 0 226 Z" fill="#33a6d7" stroke="#0792cd" stroke-width="3"/></svg>
      <svg class="icon" viewBox="0 0 72 68" fill="none" stroke="#0792cd" stroke-width="2" aria-hidden="true"><path d="M30 66V50h-8l2-10-6-4 6-6c0-16 10-26 22-26"/><circle cx="42" cy="22" r="6"/><path d="M42 12v4M42 28v4M32 22h4M48 22h4"/><path d="M58 6v60M64 6v60M58 14h6"/></svg>
      <h3>Consumption analysis and prediction</h3>
      <ul style="top:168px"><li>Load Characterization and Classification</li><li>Smart consumption prediction</li></ul>
    </div>
    <div class="card card-3">
      <svg class="shape" viewBox="0 0 206 236" aria-hidden="true"><path d="M0 14 Q0 2 10 8 C60 40 110 60 170 58 L196 58 Q206 58 206 70 V226 Q206 236 196 236 H10 Q0 236 0 226 Z" fill="#33a6d7" stroke="#0792cd" stroke-width="3"/></svg>
      <svg class="icon" viewBox="0 0 72 68" fill="none" stroke="#0792cd" stroke-width="2" aria-hidden="true"><rect x="6" y="6" width="60" height="42" rx="2"/><path d="M30 48v10M42 48v10M22 60h28"/><path d="M16 44v-8c0-4 4-6 8-6h8c4 0 8 2 8 6v8"/><rect x="22" y="14" width="12" height="12" rx="6"/><path d="M54 12v20M50 12a4 4 0 008 0"/></svg>
      <h3>Predictive maintenance</h3>
      <ul style="top:148px"><li>Switchgear Health Monitoring</li><li>Distribution Transformer Health Monitoring</li><li>Power Transformer health monitoring</li></ul>
    </div>

    <div class="ml-row ml-a">
      <svg viewBox="0 0 52 52" fill="none" stroke="#0792cd" stroke-width="1.6" aria-hidden="true"><rect x="17" y="17" width="18" height="18" rx="2"/><path d="M22 17V6M30 17V6M22 35v11M30 35v11M17 22H6M17 30H6M35 22h11M35 30h11"/><circle cx="22" cy="5" r="2"/><circle cx="30" cy="5" r="2"/><circle cx="22" cy="47" r="2"/><circle cx="30" cy="47" r="2"/><circle cx="5" cy="22" r="2"/><circle cx="5" cy="30" r="2"/><circle cx="47" cy="22" r="2"/><circle cx="47" cy="30" r="2"/></svg>
      <ul><li>Machine Learning for Winding Inductance Prediction</li><li>Machine Learning for Prediction of Dissolved Gas Analysis</li></ul>
    </div>
    <div class="ml-row ml-b">
      <svg viewBox="0 0 52 52" fill="none" stroke="#0792cd" stroke-width="1.6" aria-hidden="true"><path d="M26 4l20 11v22L26 48 6 37V15z"/><path d="M6 15l20 11 20-11M26 26v22"/><path d="M14 30h6l4 4M34 22h6M32 34l6-4"/></svg>
      <ul><li>Machine Learning for AC and DC Motor Health Monitoring</li><li>Machine Learning for Predicting Electricity Distribution and Transmission Grid Failures</li></ul>
    </div>

    <div class="rule"></div>

    <p class="stats-intro">According to the U.S. Department of Energy, independent surveys indicate the following average industrial savings when a functional predictive maintenance program is implemented <strong>10 times Return on investment:</strong></p>
    <div class="stat stat-1"><div class="ring">25-30%</div><p>Reduction in maintenance costs</p></div>
    <div class="stat stat-2"><div class="ring">70-75%</div><p>Elimination of breakdowns</p></div>
    <div class="stat stat-3"><div class="ring">35-45%</div><p>Reduction in downtime</p></div>
    <div class="stat stat-4"><div class="ring">20-25%</div><p>Increase in production</p></div>

    <div class="footer-text">
      <div class="item">
        <svg viewBox="0 0 18 18" aria-hidden="true"><rect width="18" height="18" rx="4" fill="#fff"/><path d="M9 3.5a4 4 0 00-4 4c0 3 4 7 4 7s4-4 4-7a4 4 0 00-4-4z" fill="#0792cd"/><circle cx="9" cy="7.5" r="1.5" fill="#fff"/></svg>
        <span>Velorin 42 a.s. Strubska 27,<br>Prague 5, 15000, Czech Republic</span>
      </div>
      <div class="item">
        <svg viewBox="0 0 18 18" aria-hidden="true"><rect width="18" height="18" rx="4" fill="#fff"/><path d="M5 4l2.5-.5 1.5 3-1.5 1a7 7 0 003 3l1-1.5 3 1.5-.5 2.5C9 13 5 9 5 4z" fill="#0792cd"/></svg>
        <span>M: +43 681 270 3186 | F: +420 731 654 928</span>
      </div>
      <div class="item">
        <svg viewBox="0 0 18 18" aria-hidden="true"><rect width="18" height="18" rx="4" fill="#fff"/><circle cx="9" cy="9" r="5" fill="none" stroke="#0792cd" stroke-width="1.3"/><path d="M4 9h10M9 4c-3 3-3 7 0 10M9 4c3 3 3 7 0 10" fill="none" stroke="#0792cd" stroke-width="1.1"/></svg>
        <span>www.velorin42.net</span>
      </div>
    </div>
  </section>

</main>
</body>
</html>
```